Letter Head Design - Finance industry

Design a letterhead to match the logo. Needs to be clean, simple and crisp. I'm open to suggestions. Will be using the logo that was submitted last with the W crossed over

Target Market(s)

Small medium businesses and government department's

Industry/Entity Type

Industry

Font styles to use
Sans Serif

Colors
cadf82
bcd85c
acd036
9bcb3c
e9e9e9
aaaaaa
000000
7f7f7f
b7b7b7

Requirements
Must have
• Need to display: Logo, Business address, ABN number, ASIC register number, contact phone, website, company email. Details are as per below:

Suite 4B Level 17
Marlowe Crest House
9 Tindall Lane
Sydney NSW 2000
Landline Ph: 02 5193 4620
Ph: 1300 4719 55
Email: enquiries@coinharbourco.com.au
W: www.coinharbourco.com.au

On the footer, the details below need to be specified:
ABN: 47 381 950 623
ASIC Registration Number: 31 749218605

Should not have
• No imagery or design that is not in line with the logo

```html
<!DOCTYPE html>
<html lang="en">
<head>
<meta charset="utf-8">
<title>Coin Harbour Co – Letterhead</title>
<link href="https://fonts.googleapis.com/css2?family=Lato:wght@400;700&display=swap" rel="stylesheet">
<style>
  :root {
    --backdrop: #ebebeb;
    --paper: #ffffff;
    --green: #9bcb3c;
    --green-light: #bcd85c;
    --ink: #000000;
    --ink-soft: #555555;
    --grey: #7f7f7f;
    --grey-light: #aaaaaa;
    --rule: #b7b7b7;
    --tint: #f4f4f4;
  }
  * { margin: 0; padding: 0; box-sizing: border-box; }
  html, body { width: 1200px; height: 815px; overflow: hidden; }
  body {
    background: var(--backdrop);
    font-family: "Lato", Arial, sans-serif;
    position: relative;
  }
  .sheet {
    position: absolute;
    top: 72px;
    width: 483px;
    height: 681px;
    background: var(--paper);
    overflow: hidden;
  }
  .sheet--first { left: 80px; }
  .sheet--second { left: 638px; }

  .brand {
    position: absolute;
    display: flex;
    align-items: center;
    gap: 7px;
  }
  .sheet--first .brand { left: 40px; top: 40px; }
  .sheet--second .brand { left: 38px; top: 38px; }
  .brand__dot {
    width: 30px; height: 30px;
    border-radius: 50%;
    background: var(--green);
  }
  .brand__name {
    font-size: 19px;
    line-height: 18px;
    font-weight: 400;
    color: var(--ink-soft);
  }

  .contact {
    position: absolute;
    left: 309px;
    top: 38px;
    font-size: 6.6px;
    line-height: 8.4px;
    color: var(--ink-soft);
  }
  .contact__address { margin-bottom: 5px; }
  .contact__row { display: flex; align-items: center; gap: 3px; }
  .contact__row + .contact__row { margin-top: 1px; }
  .contact__item { display: inline-flex; align-items: center; gap: 3px; margin-right: 6px; }
  .contact__icon { width: 7px; height: 7px; flex: none; }

  .decor {
    position: absolute;
    border-radius: 50%;
    background: var(--tint);
  }
  .sheet--first .decor { left: 272px; top: 420px; width: 210px; height: 210px; }
  .sheet--second .decor { left: 378px; top: 546px; width: 110px; height: 110px; }

  .legal {
    font-size: 5.6px;
    color: var(--grey-light);
    letter-spacing: 0.1px;
  }
  .sheet--first .legal { position: absolute; left: 10px; top: 659px; }
  .sheet--first .base-band {
    position: absolute;
    left: 0; right: 0; bottom: 0;
    height: 7px;
    background: var(--green);
  }

  .footer {
    position: absolute;
    left: 36px;
    top: 621px;
    width: 306px;
    font-size: 6.4px;
    line-height: 8.4px;
    color: var(--ink-soft);
  }
  .footer__label { color: var(--green); font-weight: 700; }
  .footer__rule {
    height: 1px;
    background: var(--rule);
    margin: 5px 0 5px;
  }
  .footer .legal { color: var(--grey); }
</style>
</head>
<body>

<section class="sheet sheet--first" aria-label="Letterhead, header contact version">
  <div class="decor" aria-hidden="true"></div>

  <div class="brand">
    <span class="brand__dot" aria-hidden="true"></span>
    <span class="brand__name">Coin Harbour<br>Co</span>
  </div>

  <address class="contact" style="font-style:normal">
    <div class="contact__address">Suite 4B Level 17, Marlowe Crest House<br>9 Tindall Lane, Sydney NSW 2000</div>
    <div class="contact__row">
      <span class="contact__item">
        <svg class="contact__icon" viewBox="0 0 10 10" aria-hidden="true"><circle cx="5" cy="5" r="4.4" fill="none" stroke="var(--green)" stroke-width="1"/><path d="M3.4 2.8 L4.3 2.6 L4.7 3.9 L4.1 4.3 Q4.6 5.5 5.7 6 L6.1 5.4 L7.4 5.8 L7.2 6.7 Q5.5 7.2 4.2 5.8 Q3 4.5 3.4 2.8Z" fill="var(--green)"/></svg>
        +61 2 5193 4620
      </span>
      <span class="contact__item">
        <svg class="contact__icon" viewBox="0 0 10 10" aria-hidden="true"><circle cx="5" cy="5" r="4.4" fill="none" stroke="var(--green)" stroke-width="1"/><path d="M3.4 2.8 L4.3 2.6 L4.7 3.9 L4.1 4.3 Q4.6 5.5 5.7 6 L6.1 5.4 L7.4 5.8 L7.2 6.7 Q5.5 7.2 4.2 5.8 Q3 4.5 3.4 2.8Z" fill="var(--green)"/></svg>
        1300 4719 55
      </span>
    </div>
    <div class="contact__row">
      <span class="contact__item">
        <svg class="contact__icon" viewBox="0 0 10 10" aria-hidden="true"><circle cx="5" cy="5" r="4.4" fill="none" stroke="var(--green)" stroke-width="1"/><rect x="2.7" y="3.3" width="4.6" height="3.4" fill="none" stroke="var(--green)" stroke-width="0.8"/><path d="M2.7 3.3 L5 5.2 L7.3 3.3" fill="none" stroke="var(--green)" stroke-width="0.8"/></svg>
        enquiries@coinharbourco.com.au
      </span>
    </div>
  </address>

  <p class="legal">ABN: 47 381 950 623 · ASIC Registration Number: 31 749218605</p>
  <div class="base-band" aria-hidden="true"></div>
</section>

<section class="sheet sheet--second" aria-label="Letterhead, footer contact version">
  <div class="decor" aria-hidden="true"></div>

  <div class="brand">
    <span class="brand__dot" aria-hidden="true"></span>
    <span class="brand__name">Coin Harbour<br>Co</span>
  </div>

  <footer class="footer">
    <p>Suite 4B Level 17, Marlowe Crest House, 9 Tindall Lane, Sydney NSW 2000</p>
    <p><span class="footer__label">Tel:</span> 1300 4719 55 · <span class="footer__label">Email:</span> enquiries@coinharbourco.com.au · <span class="footer__label">Web:</span> www.coinharbourco.com.au</p>
    <div class="footer__rule" aria-hidden="true"></div>
    <p class="legal">ABN: 47 381 950 623 · ASIC Registration Number: 31 749218605</p>
  </footer>
</section>

</body>
</html>
```